Flyer Handout when attending Dental Conventions, or dental office shows

take the sample file folder that is shown with 2 pictures. The outside and inside of the folder needs to be completed, along with the inserts. This folder pictures are from someone elses flyer/folder and i would like to have it layout like this. The KPW inserts is informational, but it is lacking originality, pictures, etc. Try to make our information and move it to 2017. When this is done, i would like to take this flyer and load it to the web or allow to send via email and make it interactive. The user can select the flyers and it will slide or flip to the flyer. this will make if kewl/fun

Target Market(s)

Dental Offices

Industry/Entity Type

Dental

Font styles to use
Serif
Sans Serif

Colors

Designer to choose colors to be used in the design.

Requirements
Must have
• a Semi new look and feel of our flyers, and a new envelope created

```html
<!DOCTYPE html>
<html lang="en">
<head>
<meta charset="utf-8">
<title>KPW Presentation Folder</title>
<link rel="stylesheet" href="https://fonts.googleapis.com/css2?family=Ubuntu:wght@400;500;700&display=swap">
<style>
  :root {
    --stage: #58595b;
    --sheet: #ffffff;
    --blue: #2196d3;
    --blue-mid: #1e86bf;
    --blue-deep: #1a6a9a;
    --orange: #f7941d;
    --ink: #1a1a1a;
    --rail: #d1d3d4;
    --dieline: #e8483b;
    --fold: #3fae49;
    --photo-light: #f2d9cc;
    --photo-mid: #d9a58f;
    --photo-cool: #a9cbe0;
    --ring: #3a3a3a;
  }
  html, body {
    margin: 0;
    padding: 0;
    width: 1200px;
    height: 800px;
    overflow: hidden;
    background: var(--stage);
  }
  .folder-art {
    display: block;
    width: 1200px;
    height: 800px;
    font-family: "Ubuntu", sans-serif;
  }
  .stage { fill: var(--stage); }
  .sheet { fill: var(--sheet); }
  .panel-blue { fill: var(--blue-mid); }
  .panel-bright { fill: var(--blue); }
  .panel-deep { fill: var(--blue-deep); }
  .accent-orange { fill: var(--orange); }
  .pocket { fill: var(--blue); }
  .pocket-rail { fill: var(--rail); }
  .card-slit { stroke: #ffffff; stroke-width: 1.2; opacity: .8; }
  .dieline { fill: none; stroke: var(--dieline); stroke-width: 1; stroke-dasharray: 5 3; }
  .fold-line { stroke: var(--fold); stroke-width: 1; stroke-dasharray: 3 3; }
  .safe-line { fill: none; stroke: #9fd3ef; stroke-width: .8; }
  .photo-ring { stroke: var(--ring); stroke-width: 6; }
  .tagline { fill: #ffffff; font-size: 22px; font-weight: 400; text-anchor: middle; }
  .contact { fill: var(--ink); font-size: 17px; font-weight: 500; }
  .tollfree-label { fill: #ffffff; font-size: 20px; font-weight: 500; text-anchor: middle; }
  .tollfree-number { fill: #ffffff; font-size: 30px; font-weight: 700; text-anchor: middle; }
  .brand-name { fill: var(--blue); font-size: 66px; font-weight: 700; text-anchor: middle; }
</style>
</head>
<body>
<svg class="folder-art" viewBox="0 0 1500 1000" xmlns="http://www.w3.org/2000/svg">
  <defs>
    <linearGradient id="photoWarm" x1="0" y1="0" x2="1" y2="1">
      <stop offset="0" stop-color="var(--photo-light)"/>
      <stop offset="1" stop-color="var(--photo-mid)"/>
    </linearGradient>
    <linearGradient id="photoCool" x1="0" y1="0" x2="1" y2="1">
      <stop offset="0" stop-color="var(--photo-cool)"/>
      <stop offset="1" stop-color="var(--photo-mid)"/>
    </linearGradient>
    <linearGradient id="edgeFade" x1="0" y1="0" x2="1" y2="0">
      <stop offset="0" stop-color="#ffffff" stop-opacity="0"/>
      <stop offset="1" stop-color="#d8dadc"/>
    </linearGradient>
  </defs>

  <rect class="stage" width="1500" height="1000"/>
  <rect class="sheet" x="161" y="30" width="1178" height="940"/>

  <!-- back cover panel -->
  <g class="back-cover">
    <polygon class="panel-bright" points="208,35 750,35 750,42 362,222 208,308"/>
    <polygon class="panel-deep" points="208,75 370,215 208,308"/>
    <polygon class="accent-orange" points="360,222 750,40 420,204"/>
    <polygon class="panel-blue" points="555,135 750,45 750,285"/>
    <polygon class="panel-blue" points="550,630 750,465 750,717 662,717"/>
    <rect class="safe-line" x="228" y="52" width="503" height="643"/>
    <text class="tagline" x="380" y="86">Bridging the Gap</text>
    <text class="tagline" x="380" y="114">Between Payers</text>
    <text class="tagline" x="380" y="142">and Providers</text>
    <text class="contact" x="248" y="594">218 Harbor Lane</text>
    <text class="contact" x="248" y="616">Maplewood, MN 55109</text>
    <text class="contact" x="248" y="638">Tel: 651-555-0142</text>
    <text class="contact" x="248" y="660">Fax: 651-555-0187</text>
    <text class="contact" x="248" y="682">www.kpwdental.com</text>
    <g role="img" aria-label="Photo cluster: smiling teeth with dental mirror, woman holding her cheek, child at a dental exam">
      <circle class="photo-ring" cx="400" cy="340" r="86" fill="url(#photoWarm)"/>
      <circle class="photo-ring" cx="490" cy="478" r="68" fill="url(#photoCool)"/>
      <circle class="photo-ring" cx="570" cy="335" r="94" fill="url(#photoWarm)"/>
    </g>
  </g>

  <!-- front cover panel -->
  <g class="front-cover">
    <polygon fill="url(#edgeFade)" points="1150,250 1293,250 1293,450 1150,520"/>
    <polygon class="accent-orange" points="750,35 998,35 998,160"/>
    <polygon class="panel-blue" points="750,55 940,130 750,285"/>
    <polygon class="panel-blue" points="750,465 945,612 775,705 750,705"/>
    <polygon class="panel-bright" points="750,717 1140,528 1293,440 1293,717"/>
    <polygon class="accent-orange" points="755,714 1140,526 1120,548"/>
    <polygon class="panel-deep" points="1130,540 1293,440 1293,680"/>
    <rect class="safe-line" x="769" y="52" width="504" height="643"/>
    <text class="brand-name" x="1140" y="128">KPW</text>
    <text class="tollfree-label" x="1091" y="645">Toll Free</text>
    <text class="tollfree-number" x="1091" y="678">800-555-0136</text>
    <g role="img" aria-label="Photo cluster: woman holding her cheek, smiling teeth with dental mirror, child at a dental exam">
      <circle class="photo-ring" cx="1080" cy="340" r="86" fill="url(#photoWarm)"/>
      <circle class="photo-ring" cx="990" cy="478" r="68" fill="url(#photoCool)"/>
      <circle class="photo-ring" cx="930" cy="335" r="94" fill="url(#photoWarm)"/>
    </g>
  </g>

  <!-- inside pockets -->
  <g class="pockets">
    <rect class="pocket-rail" x="210" y="717" width="36" height="251"/>
    <rect class="pocket-rail" x="1254" y="717" width="36" height="251"/>
    <path class="pocket" d="M258,732 H720 L700,880 Q690,948 640,948 H258 Z"/>
    <path class="pocket" d="M780,732 H1243 V948 H860 Q810,948 800,880 Z"/>
    <line class="card-slit" x1="375" y1="815" x2="410" y2="782"/>
    <line class="card-slit" x1="543" y1="782" x2="578" y2="815"/>
    <line class="card-slit" x1="375" y1="866" x2="410" y2="900"/>
    <line class="card-slit" x1="543" y1="900" x2="578" y2="866"/>
  </g>

  <!-- die and fold marks -->
  <g class="marks">
    <line class="fold-line" x1="208" y1="35" x2="208" y2="717"/>
    <line class="fold-line" x1="1293" y1="35" x2="1293" y2="717"/>
    <path class="dieline" d="M208,35 H165 V440 A22,22 0 0 1 165,482 V690 L208,712"/>
    <path class="dieline" d="M1293,35 H1336 V440 A22,22 0 0 0 1336,482 V690 L1293,712"/>
    <path class="dieline" d="M210,717 V968 H690 Q735,955 745,717"/>
    <path class="dieline" d="M1290,717 V968 H810 Q765,955 755,717"/>
  </g>
</svg>
</body>
</html>
```